Tidewell Metrics Group Company Website Design and Coding

We want to redesign our existing website so that it is more visually and functionally appealing to prospective clients and potential job candidates. We would like to keep our current color scheme and implement our current logo as well. We have a high-level idea of website structure that we are thinking of, which is in the attached files. Logo is included as well. The final design would ideally be energy and analytics focused. We will need the new website to be coded as well, please.

Target Market(s)

Energy and utility industry

Industry/Entity Type

Energy/analytics

Coding

Coded - Design and coding required

Number of Pages Required

5+ page

Font styles to use
Sans Serif

Colors
0094D4
00A9DD
6FCCEA
C7EBF8
E9F6FB
F0912C
F2A743
F7CA91
FBE8D2
FDF5EE

Requirements
Must have
• Consistent color scheme- please use the one that we provided. We need an overview, a home page, and our core services. A separate job application page. Logo must be incorporated. We would like e "Meet our Team" page. Please include all of the content that is listed in our attachments.
Nice to have
• Movement
Should not have
• No music, no cartoons/animation, no pictures of a chalkboard

```html
<!DOCTYPE html>
<html lang="en">
<head>
<meta charset="utf-8">
<title>Tidewell Metrics Group</title>
<link rel="stylesheet" href="https://fonts.googleapis.com/css2?family=Barlow:wght@300;400;500;600;700&display=swap">
<style>
:root{
  --blue:#0094D4;
  --blue-2:#00A9DD;
  --blue-3:#6FCCEA;
  --blue-4:#C7EBF8;
  --blue-5:#E9F6FB;
  --orange:#F0912C;
  --orange-2:#F2A743;
  --orange-3:#F7CA91;
  --ink:#111111;
  --muted:#555a60;
  --white:#ffffff;
  --footer:#000000;
}
*{margin:0;padding:0;box-sizing:border-box}
html,body{width:1200px;height:2679px;overflow:hidden}
body{font-family:"Barlow",Arial,sans-serif;color:var(--ink);background:var(--white);position:relative}
.abs{position:absolute}
a{color:inherit;text-decoration:none}

/* header */
.site-header{position:absolute;left:0;top:0;width:1200px;height:75px;background:var(--white);z-index:5}
.brand{position:absolute;left:93px;top:14px;display:flex;align-items:flex-start;gap:10px}
.brand-mark{width:36px;height:36px;border-radius:50%;background:var(--blue-4);margin-top:2px}
.brand-name{font-size:23px;font-weight:400;color:var(--blue);line-height:1.1;letter-spacing:.2px}
.brand-tag{font-size:8.5px;letter-spacing:2.2px;color:#8a8f96;margin-top:4px}
.main-nav{position:absolute;top:28px;font-size:13px;font-weight:600;color:var(--ink)}
.main-nav span{position:absolute;white-space:nowrap}
.main-nav .active{color:var(--blue)}
.caret{display:inline-block;width:5px;height:5px;border-right:1.5px solid currentColor;border-bottom:1.5px solid currentColor;transform:rotate(45deg);margin-left:6px;position:relative;top:-3px}
.nav-phone{position:absolute;left:866px;top:27px;color:var(--blue);font-size:13px;font-weight:600;display:flex;align-items:center;gap:6px}
.btn-contact{position:absolute;left:994px;top:19px;width:112px;height:37px;background:var(--orange-2);color:var(--white);font-size:13px;font-weight:600;display:flex;align-items:center;justify-content:center}

.dropdown{position:absolute;left:535px;top:75px;width:234px;background:var(--blue-2);z-index:6}
.dropdown div{height:37.5px;padding-left:22px;display:flex;align-items:center;color:var(--white);font-size:10px;font-weight:500;border-bottom:1px solid rgba(255,255,255,.35)}
.dropdown div:last-child{border-bottom:none}
.dropdown .on{background:var(--orange-2)}

/* hero */
.hero{position:absolute;left:0;top:75px;width:1200px;height:437px;
  background:
    radial-gradient(ellipse 260px 180px at 480px 110px,rgba(235,238,242,.85),rgba(235,238,242,0) 70%),
    radial-gradient(ellipse 300px 160px at 560px 320px,rgba(60,62,66,.9),rgba(60,62,66,0) 75%),
    radial-gradient(ellipse 200px 260px at 1050px 150px,rgba(90,150,110,.55),rgba(90,150,110,0) 70%),
    radial-gradient(ellipse 260px 200px at 880px 330px,rgba(225,205,190,.8),rgba(225,205,190,0) 70%),
    radial-gradient(ellipse 260px 200px at 100px 330px,rgba(150,140,135,.8),rgba(150,140,135,0) 70%),
    linear-gradient(180deg,#7a5a48 0%,#b9b7b4 30%,#d6d4d0 70%,#a9a6a2 100%)}
.hero-shade{position:absolute;inset:0;background:rgba(15,17,20,.5)}
.hero h1{position:absolute;left:200px;top:138px;font-size:30px;font-weight:700;color:var(--white);white-space:nowrap}
.hero p{position:absolute;left:200px;top:182px;width:640px;font-size:21px;font-weight:400;line-height:27px;color:var(--white)}
.btn-blue{position:absolute;left:200px;top:256px;width:124px;height:36px;background:var(--blue);color:var(--white);font-size:12px;font-weight:600;display:flex;align-items:center;justify-content:center}
.dots{position:absolute;left:990px;top:183px}
.dots i{display:block;width:11px;height:11px;border:1.5px solid var(--white);border-radius:50%;margin-bottom:9.5px;position:relative}
.dots i.on::after{content:"";position:absolute;left:2px;top:2px;width:4px;height:4px;border-radius:50%;background:var(--white)}

/* shared */
.section-title{font-size:30px;font-weight:400;text-align:center}
.section-title b{font-weight:700}
.body-copy{font-size:11px;line-height:19px;color:var(--muted);text-align:center}
.btn-outline{position:absolute;border:2px solid var(--orange);color:var(--ink);font-size:12px;font-weight:600;display:flex;align-items:center;justify-content:center;background:transparent}
.deco{position:absolute;border-radius:50% 40% 55% 45%;background:radial-gradient(ellipse at 40% 35%,rgba(0,148,212,.55),rgba(0,169,221,.15) 60%,rgba(0,169,221,0) 75%)}

/* welcome */
.welcome{position:absolute;left:0;top:512px;width:1200px;height:328px}
.welcome .section-title{position:absolute;left:0;top:55px;width:1200px}
.welcome .body-copy{position:absolute;left:215px;top:110px;width:770px}

/* services */
.services{position:absolute;left:0;top:840px;width:1200px;height:482px;
  background:
    radial-gradient(ellipse 220px 160px at 640px 180px,rgba(230,160,90,.75),rgba(230,160,90,0) 70%),
    radial-gradient(ellipse 200px 150px at 420px 420px,rgba(200,120,70,.55),rgba(200,120,70,0) 70%),
    radial-gradient(ellipse 260px 220px at 980px 230px,rgba(235,238,242,.75),rgba(235,238,242,0) 70%),
    linear-gradient(100deg,#2e3033 0%,#4a3f38 28%,#7a6a5e 48%,#9a9da1 68%,#c8cbcf 82%,#5e6064 100%)}
.services .shade{position:absolute;inset:0;background:linear-gradient(90deg,rgba(25,25,28,.62),rgba(25,25,28,.2))}
.services h2{position:absolute;left:200px;top:55px;font-size:30px;font-weight:700;color:var(--white)}
.service-list{position:absolute;left:200px;top:133px;list-style:none}
.service-list li{height:37.5px;font-size:22px;color:var(--white);padding-left:22px;position:relative;line-height:37.5px}
.service-list li::before{content:"";position:absolute;left:0;top:14px;border-left:5px solid var(--white);border-top:4px solid transparent;border-bottom:4px solid transparent}
.btn-orange{position:absolute;left:200px;top:379px;width:118px;height:37px;background:var(--orange);color:var(--white);font-size:12px;font-weight:600;display:flex;align-items:center;justify-content:center}

/* case studies */
.cases{position:absolute;left:0;top:1322px;width:1200px;height:710px;background:var(--blue-5)}
.cases-title{position:absolute;left:198px;top:56px;font-size:30px;font-weight:300;line-height:38px}
.cases-title b{font-weight:700}
.case-img{position:absolute}
.case-img .label{position:absolute;left:24px;top:22px;color:var(--white);font-size:13px;font-weight:700;text-shadow:0 1px 2px rgba(0,0,0,.35)}
.img-office{background:
  radial-gradient(ellipse 120px 80px at 110px 110px,rgba(40,42,46,.8),rgba(40,42,46,0) 70%),
  radial-gradient(ellipse 160px 90px at 250px 150px,rgba(235,232,226,.9),rgba(235,232,226,0) 70%),
  radial-gradient(ellipse 140px 80px at 260px 40px,rgba(60,80,120,.75),rgba(60,80,120,0) 70%),
  linear-gradient(160deg,#6e6a64 0%,#b9b4ac 45%,#d8d3ca 70%,#8d877f 100%)}
.img-phone{background:
  radial-gradient(ellipse 140px 60px at 200px 120px,rgba(200,170,150,.8),rgba(200,170,150,0) 70%),
  radial-gradient(ellipse 90px 120px at 340px 60px,rgba(25,28,32,.85),rgba(25,28,32,0) 75%),
  linear-gradient(120deg,#8a8c90 0%,#b6b8bb 40%,#6d7074 75%,#2f3236 100%)}
.img-support{background:
  radial-gradient(ellipse 90px 80px at 150px 80px,rgba(170,120,95,.7),rgba(170,120,95,0) 70%),
  radial-gradient(ellipse 80px 110px at 340px 90px,rgba(40,44,50,.8),rgba(40,44,50,0) 75%),
  radial-gradient(ellipse 140px 60px at 250px 30px,rgba(235,225,210,.9),rgba(235,225,210,0) 70%),
  linear-gradient(160deg,#c9c2b6 0%,#a6a39e 50%,#5b5f66 100%)}
.case-strip{position:absolute;background:#3d4247;width:25px}
.case-box{position:absolute;background:var(--white);padding:20px 24px}
.case-box h3{font-size:18px;font-weight:400;line-height:22px}
.case-box p{font-size:9.5px;line-height:14px;margin-top:14px;color:var(--ink);width:320px}

/* jobs */
.jobs{position:absolute;left:0;top:2032px;width:1200px;height:308px}
.jobs .section-title{position:absolute;left:0;top:55px;width:1200px}
.jobs .body-copy{position:absolute;left:210px;top:110px;width:780px}

/* footer */
.site-footer{position:absolute;left:0;top:2340px;width:1200px;height:339px;background:var(--footer);color:var(--white)}
.site-footer h4{position:absolute;top:65px;font-size:15px;font-weight:600}
.f-item{position:absolute;left:200px;font-size:11px;display:flex;align-items:flex-start;gap:13px}
.f-item svg{flex:none;margin-top:1px}
.quick{position:absolute;left:494px;top:94px;list-style:none;font-size:10px;line-height:22.7px}
.sub-input{position:absolute;left:750px;top:97px;width:250px;height:37px;border:1.5px solid var(--white);font-size:10px;padding-left:12px;display:flex;align-items:center}
.sub-btn{position:absolute;left:750px;top:143px;width:100px;height:37px;background:var(--orange);font-size:12px;font-weight:600;display:flex;align-items:center;justify-content:center}
.social{position:absolute;top:257px;width:30px;height:30px;border:1.5px solid var(--orange);display:flex;align-items:center;justify-content:center}
.social::after{content:"";width:7px;height:7px;border-radius:50%;background:var(--orange)}
.social.on{background:var(--orange)}
.social.on::after{background:var(--white)}
.copyright{position:absolute;left:200px;top:265px;font-size:10px}
.copyright span{color:var(--blue-2)}
</style>
</head>
<body>

<header class="site-header">
  <div class="brand">
    <div class="brand-mark"></div>
    <div>
      <div class="brand-name">Tidewell Metrics Group</div>
      <div class="brand-tag">DATA DRIVEN RESEARCH AND INSIGHTS</div>
    </div>
  </div>
  <nav class="main-nav">
    <span style="left:473px">Home</span>
    <span class="active" style="left:534px">Core Services<i class="caret"></i></span>
    <span style="left:650px">About Us<i class="caret"></i></span>
    <span style="left:740px">Our Work</span>
    <span style="left:819px">Blog</span>
  </nav>
  <div class="nav-phone">
    <svg width="13" height="13" viewBox="0 0 24 24" fill="none" stroke="currentColor" stroke-width="2.4"><path d="M5 3h4l2 5-3 2a12 12 0 0 0 6 6l2-3 5 2v4a2 2 0 0 1-2 2A17 17 0 0 1 3 5a2 2 0 0 1 2-2z"/></svg>
    555.318.2047
  </div>
  <a class="btn-contact">Contact Us</a>
</header>

<div class="dropdown">
  <div>Predictive Analytics and Forecasting</div>
  <div class="on">T&amp;D Planning</div>
  <div>Evaluation</div>
  <div>Pilot &amp; Emerging Tech Support</div>
  <div>Program Portfolio &amp; Resource Planning</div>
  <div>Program Delivery Support</div>
</div>

<section class="hero" role="img" aria-label="Business people reviewing charts on a laptop at a desk">
  <div class="hero-shade"></div>
  <h1>Tidewell Metrics Group is a Research Company</h1>
  <p>That helps utilities and regulatory agencies navigate the challenges of building a smarter and cleaner energy future.</p>
  <a class="btn-blue">Explore More</a>
  <div class="dots"><i></i><i class="on"></i><i></i><i></i></div>
</section>

<section class="welcome">
  <div class="deco" style="left:43px;top:143px;width:172px;height:185px" role="img" aria-label="Decorative dotted wave ribbon"></div>
  <h2 class="section-title">Welcome to <b>Tidewell Metrics Group</b></h2>
  <p class="body-copy">Tidewell Metrics Group (TMG) was formed in 2016 to help utilities and regulatory agencies navigate the technical, economic, and policy challenges of building a smarter and cleaner energy future. Our research focuses on impact analysis as well as predictive and causal analytics. We deliver data-driven insights into how various technologies and interventions affect the way homes and businesses use energy and how those in turn affect grid and system planning. We have a proven record for conducting high-quality, accurate, and unbiased analysis and are meticulous about ensuring that research is useful for policy decisions, operations, and implementation.</p>
  <a class="btn-outline" style="left:529px;top:229px;width:123px;height:37px">Discover More</a>
</section>

<section class="services" role="img" aria-label="Hands using a tablet with overlaid analytics bar charts and trend lines">
  <div class="shade"></div>
  <h2>Services We Provide</h2>
  <ul class="service-list">
    <li>Predictive Analytics and Forecasting</li>
    <li>T&amp;D Planning</li>
    <li>Evaluation</li>
    <li>Pilot &amp; Emerging Tech Support</li>
    <li>Program Portfolio &amp; Resource Planning</li>
    <li>Program Delivery Support</li>
  </ul>
  <a class="btn-orange">Explore More</a>
</section>

<section class="cases">
  <h2 class="cases-title">Tidewell Metrics Group<br><b>Case Studies</b></h2>

  <div class="case-img img-office" style="left:200px;top:173px;width:387px;height:250px" role="img" aria-label="Team reviewing printed charts around a laptop"><span class="label">T&amp;D Planning</span></div>
  <div class="case-strip" style="left:200px;top:423px;height:63px"></div>
  <div class="case-box" style="left:225px;top:423px;width:362px;height:130px">
    <h3>Meter-Based Methods from<br>Coast to Coast</h3>
    <p>Tidewell Metrics Group (TMG) recently conducted two similar studies on the accuracy of using smart meter data for evaluation and settlement of energy efficiency ...</p>
  </div>

  <div class="case-img img-phone" style="left:612px;top:63px;width:388px;height:156px" role="img" aria-label="Hand using a phone with star ratings overlay"><span class="label">Evaluation</span></div>
  <div class="case-strip" style="left:612px;top:219px;height:62px"></div>
  <div class="case-box" style="left:637px;top:219px;width:363px;height:62px;padding-top:14px">
    <h3>Does residential battery storage<br>help the grid?</h3>
  </div>

  <div class="case-img img-support" style="left:612px;top:339px;width:388px;height:156px" role="img" aria-label="Support staff wearing headsets at computer workstations"><span class="label">Pilot &amp; Emerging Tech Support</span></div>
  <div class="case-strip" style="left:612px;top:495px;height:62px"></div>
  <div class="case-box" style="left:637px;top:495px;width:363px;height:62px;padding-top:14px">
    <h3>California Electric Vehicle Penetration –<br>Granular Maps</h3>
  </div>

  <a class="btn-outline" style="left:550px;top:607px;width:100px;height:37px">View All</a>
  <div class="deco" style="left:995px;top:528px;width:170px;height:182px" role="img" aria-label="Decorative dotted wave ribbon"></div>
</section>

<section class="jobs">
  <h2 class="section-title">Job <b>Opportunities</b></h2>
  <p class="body-copy">We are looking for candidates with strong quantitative skills and demonstrated interest in working at the intersection of analytics, data, energy, policy, and economics. Successful candidates will also have excellent written and oral communication skills and are comfortable explaining complex concepts to non-technical audiences. These positions will work closely with senior staff to produce high-quality analyses, tools, reports, and presentations for our clients, solving pressing questions about the future of the electric grid and natural gas distribution network in North America.</p>
  <a class="btn-outline" style="left:519px;top:211px;width:156px;height:37px">View Current Openings</a>
</section>

<footer class="site-footer">
  <div class="deco" style="left:0;top:120px;width:190px;height:219px;background:radial-gradient(ellipse at 55% 40%,rgba(0,148,212,.55),rgba(0,148,212,.12) 60%,rgba(0,148,212,0) 75%)" role="img" aria-label="Decorative dotted wave ribbon"></div>

  <h4 style="left:200px">Contact Us</h4>
  <div class="f-item" style="top:98px;font-size:14px">
    <svg width="12" height="12" viewBox="0 0 24 24" fill="none" stroke="#F0912C" stroke-width="2.6"><path d="M5 3h4l2 5-3 2a12 12 0 0 0 6 6l2-3 5 2v4a2 2 0 0 1-2 2A17 17 0 0 1 3 5a2 2 0 0 1 2-2z"/></svg>
    555.318.2047
  </div>
  <div class="f-item" style="top:131px">
    <svg width="11" height="11" viewBox="0 0 24 24" fill="#F0912C"><path d="M2 8l10-6 10 6v13H2z"/><path d="M4 9l8 5 8-5" stroke="#000" stroke-width="1.6" fill="none"/></svg>
    hello@tidewellmetrics.com
  </div>
  <div class="f-item" style="top:167px;line-height:17px">
    <svg width="11" height="14" viewBox="0 0 24 30" fill="#F0912C"><path d="M12 0a10 10 0 0 0-10 10c0 8 10 20 10 20s10-12 10-20A10 10 0 0 0 12 0zm0 14a4 4 0 1 1 0-8 4 4 0 0 1 0 8z"/></svg>
    <div style="font-size:10px"><span style="color:var(--orange)">Tidewell Metrics Group</span><br>412 Harbor Crest Blvd Suite 210<br>Riverton, GA 30099</div>
  </div>

  <h4 style="left:494px">Quick Links</h4>
  <ul class="quick">
    <li>Predictive Analytics and Forecasting</li>
    <li>T&amp;D Planning</li>
    <li>Evaluation</li>
    <li>Pilot &amp; Emerging Tech Support</li>
    <li>Program Portfolio &amp; Resource Planning</li>
    <li>Program Delivery Support</li>
  </ul>

  <h4 style="left:750px">Subscribe Us</h4>
  <div class="sub-input">name@email.com</div>
  <a class="sub-btn">Subscribe</a>

  <a class="social" style="left:750px" aria-label="Social profile"></a>
  <a class="social on" style="left:788px" aria-label="Social profile"></a>
  <a class="social" style="left:826px" aria-label="Social profile"></a>

  <p class="copyright">2022 <span>Tidewell Metrics Group</span>. All Rights Reserved.</p>

  <svg class="abs" style="left:1094px;top:257px" width="24" height="30" viewBox="0 0 24 30" aria-label="Back to top"><path d="M12 0L24 30 12 23 0 30z" fill="#F0912C"/></svg>
</footer>

</body>
</html>
```